We are an online mail order nursery selling live plants who needs a 1 page landing page for an upcom

We are opening a new sister site to our main site. The new site is membership based. We need a landing page for an email campaign that is both attention grabbing and simply luring the customer to click on the learn more about Membership Page : http://www.fernlanecircle.com/pages/membership-info
The landing page will need to have space reserved for a white board presentation. I have attached the video below. The vid will be hosted on Reel barn so we should be able to use the iframe / embed technique. Again our goal is to funnel the customer to http://www.fernlanecircle.com/pages/membership-info where they can get more details.

Target Market(s)

Home owners between the age of 35 and 65 - gardening enthusiast

Industry/Entity Type

Campaign

Number of Pages Required

1 page

Font styles to use
Sans Serif

Requirements
Must have
• space to embed white board video

```html
<!DOCTYPE html>
<html lang="en">
<head>
<meta charset="utf-8">
<title>Fern Lane Circle – Gold Membership</title>
<link rel="stylesheet" href="https://fonts.googleapis.com/css2?family=Open+Sans:wght@400;600&family=Roboto+Condensed:wght@700&display=swap">
<style>
  :root {
    --page-bg: #ffffff;
    --brand-green: #7bb52f;
    --band-green: #6a9c2b;
    --button-dark: #4a7619;
    --button-dark-border: #2f4d0e;
    --bullet-green: #a6e04a;
    --hero-dark: #0f2310;
    --hero-mid: #2f5a22;
    --hero-bloom: #b8476e;
    --heading-grey: #7a8087;
    --body-grey: #6f6f6f;
    --footer-grey: #555555;
    --divider: #e8e8e8;
    --card-shadow: rgba(0,0,0,0.12);
  }
  * { box-sizing: border-box; margin: 0; padding: 0; }
  html, body { width: 1200px; height: 2412px; overflow: hidden; background: var(--page-bg); }
  body { position: relative; font-family: "Open Sans", Arial, sans-serif; color: var(--body-grey); }

  .site-header { position: absolute; top: 0; left: 0; width: 1200px; height: 140px; }
  .brand { position: absolute; left: 137px; top: 52px; display: flex; align-items: center; gap: 14px; }
  .brand-mark { width: 56px; height: 56px; border-radius: 50%; background: var(--brand-green); }
  .brand-name { font-family: "Roboto Condensed", Arial, sans-serif; font-weight: 700; font-size: 38px; color: var(--brand-green); letter-spacing: 1px; }
  .pricing { position: absolute; right: 158px; top: 58px; text-align: left; font-size: 18px; line-height: 24px; color: #8a8a8a; }
  .pricing-phone { display: flex; align-items: center; gap: 6px; color: var(--brand-green); font-size: 17px; }

  .card { position: absolute; left: 84px; top: 140px; width: 1030px; height: 2071px; background: #fff; box-shadow: 0 1px 4px var(--card-shadow); border-radius: 4px; overflow: hidden; }

  .hero { position: relative; height: 498px; }
  .hero-photo { position: absolute; inset: 0; background: radial-gradient(ellipse 360px 300px at 76% 50%, var(--hero-bloom) 0%, #6b3550 35%, transparent 70%), linear-gradient(100deg, var(--hero-mid) 0%, #1d3a16 50%, var(--hero-dark) 100%); }
  .hero-title { position: absolute; left: 33px; top: 92px; font-family: "Roboto Condensed", Arial, sans-serif; font-weight: 700; font-size: 37px; line-height: 68px; color: #fff; text-transform: uppercase; }
  .hero-button { position: absolute; left: 31px; top: 325px; width: 205px; height: 49px; background: var(--brand-green); border: 2px solid #fff; border-radius: 5px; font-family: "Roboto Condensed", Arial, sans-serif; font-weight: 700; font-size: 21px; color: #1a2a0c; display: flex; align-items: center; justify-content: center; text-decoration: none; }

  .intro { text-align: center; padding-top: 52px; }
  .section-title { font-family: "Roboto Condensed", Arial, sans-serif; font-weight: 700; font-size: 31px; color: var(--heading-grey); text-transform: uppercase; }
  .intro-copy { margin: 4px auto 0; width: 960px; font-size: 21.5px; line-height: 41px; }
  .read-more { color: var(--brand-green); font-weight: 600; text-decoration: none; }
  .divider { position: absolute; left: 34px; top: 758px; width: 960px; height: 2px; background: var(--divider); }

  .video-slot { position: absolute; left: 70px; top: 811px; width: 912px; height: 532px; border-radius: 14px; background: linear-gradient(180deg, #e9ecef 0%, #d4d8dc 100%); }

  .benefits { position: absolute; left: 0; top: 1416px; width: 1030px; height: 295px; background: var(--band-green); color: #fff; }
  .benefit { position: absolute; width: 420px; font-size: 22px; line-height: 34px; padding-left: 50px; }
  .benefit::before { content: ""; position: absolute; left: 16px; top: 11px; width: 15px; height: 15px; border-radius: 50%; background: var(--bullet-green); }
  .details-button { position: absolute; left: 651px; top: 204px; width: 281px; height: 55px; background: var(--button-dark); border: 2px solid var(--button-dark-border); border-radius: 4px; font-family: "Roboto Condensed", Arial, sans-serif; font-weight: 700; font-size: 22px; color: #fff; display: flex; align-items: center; justify-content: center; text-decoration: none; }

  .referral { position: absolute; left: 0; top: 1752px; width: 1030px; text-align: center; }
  .referral-title { font-size: 29px; font-weight: 600; color: #6b6b6b; }
  .referral-copy { margin: 8px auto 0; width: 960px; font-size: 21.5px; line-height: 41px; }
  .get-button { display: flex; align-items: center; justify-content: center; margin: 20px auto 0; width: 367px; height: 61px; border: 2px solid var(--brand-green); border-radius: 4px; font-size: 23px; font-weight: 600; color: var(--brand-green); text-decoration: none; letter-spacing: 0.5px; }

  .site-footer { position: absolute; left: 0; top: 2262px; width: 1200px; text-align: center; }
  .social { display: flex; justify-content: center; gap: 26px; }
  .social a { font-size: 20px; font-weight: 600; color: var(--footer-grey); text-decoration: none; display: flex; align-items: center; gap: 8px; }
  .social a::before { content: ""; width: 14px; height: 14px; background: var(--footer-grey); border-radius: 3px; }
  .footer-note { margin-top: 22px; font-size: 21px; color: var(--footer-grey); }
  .footer-note a { color: var(--brand-green); text-decoration: none; }
</style>
</head>
<body>
  <header class="site-header">
    <div class="brand">
      <span class="brand-mark"></span>
      <span class="brand-name">FERN LANE CIRCLE</span>
    </div>
    <div class="pricing">
      <div>Call for pricing</div>
      <div class="pricing-phone">
        <svg width="16" height="14" viewBox="0 0 16 14" aria-hidden="true"><path d="M1 5 Q8 -1 15 5 L13 7 L11 5.5 L11 4 Q8 3 5 4 L5 5.5 L3 7 Z M3 8 H13 V13 H3 Z" fill="currentColor"/></svg>
        888-555-0147
      </div>
    </div>
  </header>

  <main class="card">
    <section class="hero">
      <div class="hero-photo" role="img" aria-label="Close-up photograph of a pink tropical flower with buds against a dark green blurred background"></div>
      <h1 class="hero-title">Gold Membership Play<br>Saving Money Is Equal<br>To Earning Money</h1>
      <a class="hero-button" href="http://www.fernlanecircle.com/pages/membership-info">LEARN MORE</a>
    </section>

    <section class="intro">
      <h2 class="section-title">Easy Way To Build Your Dream Garden</h2>
      <p class="intro-copy">All gardeners know that "dream" gardens like the ones you see in magazines are expensive. When you are planting a perennial border that is 5 foot wide and 40 feet long and placing the plants in groups of 3 and 5 those $14 to $20 dollar plants that <a class="read-more" href="http://www.fernlanecircle.com/pages/membership-info">--&gt;Read More</a></p>
    </section>
    <div class="divider"></div>

    <div class="video-slot" role="img" aria-label="Embedded whiteboard presentation video shown on a laptop, with calendar, presenter and wallet illustrations"></div>

    <section class="benefits">
      <p class="benefit" style="left:0;top:16px;">Save Additional 30% on the top of the half price sale for 1 year</p>
      <p class="benefit" style="left:0;top:98px;">Get half price shipping on every order no matter the size</p>
      <p class="benefit" style="left:0;top:184px;">Free returns if you are not 100% satisfied with your plants</p>
      <p class="benefit" style="left:557px;top:16px;">Invitation onlynursery liquidation / flash sales</p>
      <p class="benefit" style="left:557px;top:98px;">Earn Membership reward pointsto buy more plants</p>
      <a class="details-button" href="http://www.fernlanecircle.com/pages/membership-info">VIEW DETAILS</a>
    </section>

    <section class="referral">
      <h2 class="referral-title">Refer friends and get a free Gold Membership</h2>
      <p class="referral-copy">When you refer a friend we send them an email containing a 30% discount on all items in the catalog. (the coupon will not work on membership fees) When your friend places an order using the coupon you get 360 points which equals $15.</p>
      <a class="get-button" href="http://www.fernlanecircle.com/pages/membership-info">GET IT NOW</a>
    </section>
  </main>

  <footer class="site-footer">
    <nav class="social">
      <a href="#">Leafbook</a>
      <a href="#">Chirpline</a>
      <a href="#">Reel barn</a>
    </nav>
    <p class="footer-note">Just not on to <a href="http://www.fernlanecircle.com">fernlanecircle.com?</a>&nbsp; Unsubscribe <a href="#">here.</a></p>
  </footer>
</body>
</html>
```